Slick Web Design for Health Care Software Company

We need a new corporate web design for our company, "Brivora." We specialize in web-based cloud software geared toward helping health care professionals.

Our focus for our home site is our products and services. We want potential clients and medical boards who visit our site to have an immediate sense of professionalism and know-how. Our products are innovative, easy to use, and customizable. Users should get this feel when visiting our site.

This is a link to our previous site: www.brivorainc.example. This site is too busy, the colors are too dark, and there's too much information in each page. When creating a design, feel free to eliminate the plethora of info present in the old site.

We have a logo and content for our site that we're going to use. For each of the 7-10 products and services, there is going to be a short 1-2 paragraph excerpt on their own page, as well as a case study related to each. Other parts that can be integrated into the site are our portfolio of clients, newsletter, and about us/contact us.

Some websites to use as general inspiration:
http://www.quellsite.example/
http://www.vantrex.example/
http://www.telmaroplans.example/

Target Market(s)

Health Care Professionals from Specialty Organizations and Boards

Industry/Entity Type

Health Care

Requirements
Nice to have
• Our trademark slogan is "Turn data in knowledge, knowledge into improvement." It would be pretty sweet to integrate this idea into the design of the site.

Also, BE CREATIVE. AVOID TRADITIONAL DESIGNS. Try to exemplify innovation within clarity.
Should not have
• Avoid dark backgrounds.

```html
<!DOCTYPE html>
<html lang="en">
<head>
<meta charset="utf-8">
<title>Brivora</title>
<link href="https://fonts.googleapis.com/css2?family=Yanone+Kaffeesatz:wght@300;400;600&family=PT+Sans+Narrow:wght@400;700&family=Arimo:wght@400;700&family=Open+Sans:wght@400;600&display=swap" rel="stylesheet">
<style>
:root{
  --page:#efece0;
  --white:#ffffff;
  --nav-top:#6a4a43;
  --nav-bottom:#4e332d;
  --nav-text:#f3ece8;
  --red:#d9302a;
  --red-title:#c4161c;
  --yellow:#ffd15a;
  --green:#5f9b10;
  --green-dark:#4b7f0a;
  --gray-head:#8a9a9a;
  --gray-sub:#a4aca4;
  --text:#a09c6a;
  --link:#6b8f3a;
  --orange:#ef8a12;
  --rule:#c8c8c8;
  --footer:#f0f0f0;
  --footer-text:#6a6a6a;
}
*{margin:0;padding:0;box-sizing:border-box}
html,body{width:979px;height:1200px;overflow:hidden;background:var(--page)}
body{position:relative;font-family:"Open Sans",sans-serif}
.sheet{position:absolute;left:57px;top:13px;width:865px;height:1187px;background:var(--white);border-radius:6px 6px 0 0}
.abs{position:absolute}
.nav{left:63px;top:19px;width:853px;height:57px;background:linear-gradient(var(--nav-top),var(--nav-bottom));display:flex;align-items:center;justify-content:space-between;padding:0 14px 0 18px}
.nav a{font-family:"PT Sans Narrow",sans-serif;font-weight:700;font-size:19px;color:var(--nav-text);text-decoration:none;letter-spacing:.2px}
.nav .sep{width:1px;height:12px;background:#8c6c64}
.brand{left:78px;top:103px;display:flex;align-items:center;gap:10px;font-family:"Arimo",sans-serif;font-weight:700;font-size:32px;color:var(--red)}
.brand .mark{width:14px;height:14px;border-radius:50%;background:var(--red)}
.follow{right:80px;top:111px;display:flex;align-items:center;gap:8px;font-family:"Arimo",sans-serif;font-weight:700;font-size:15px;color:#8c8c8c}
.follow .sq{width:20px;height:20px;border-radius:3px}
.tiles{left:63px;top:168px;width:284px;height:351px}
.tile{position:relative;height:117px;padding:30px 0 0 15px;color:var(--white)}
.tile:nth-child(1){background:linear-gradient(90deg,#e8483d 0 236px,#ed6357 236px)}
.tile:nth-child(2){background:linear-gradient(90deg,#e03a31 0 236px,#e8554b 236px)}
.tile:nth-child(3){background:linear-gradient(90deg,#d62a22 0 236px,#e04840 236px)}
.tile h2{font-family:"Yanone Kaffeesatz",sans-serif;font-weight:300;font-size:36px;line-height:1;letter-spacing:-.3px}
.tile p{font-family:"PT Sans Narrow",sans-serif;font-weight:700;font-size:14px;color:var(--yellow);margin-top:4px}
.tile svg{position:absolute;right:12px;bottom:10px}
.hero{left:347px;top:162px;width:569px;height:372px;background:#eef6dc}
.hero-photo{position:absolute;left:0;top:6px;width:569px;height:351px;background:linear-gradient(100deg,#f3f4ec 0%,#e4eccf 45%,#ead6cc 100%)}
.badge{position:absolute;left:306px;top:178px;width:238px;height:132px;border-radius:50%;background:rgba(240,138,20,.92);color:var(--white);font-family:"Arimo",sans-serif;font-weight:700;font-style:italic;text-align:center;padding-top:16px;line-height:1}
.badge .s1{font-size:28px}.badge .s2{font-size:19px}.badge .s3{font-size:54px;letter-spacing:-2px}
.sec-head{font-family:"PT Sans Narrow",sans-serif;font-size:23px;line-height:1;color:var(--gray-head)}
.sec-sub{font-family:"PT Sans Narrow",sans-serif;font-size:12px;color:var(--gray-sub);margin-top:2px;letter-spacing:.2px}
.item-title{font-family:"Arimo",sans-serif;font-weight:700;font-size:15px;color:var(--red-title);display:flex;align-items:center;gap:10px}
.body{font-size:12px;line-height:20px;color:var(--text)}
.body u,.lnk{color:var(--link);text-decoration:underline}
.more{font-size:11px;color:var(--link);display:flex;align-items:center;gap:6px}
.more i{width:9px;height:9px;border-radius:50%;background:var(--green);display:inline-block}
.main-head{display:flex;gap:6px;border-bottom:1px dashed var(--rule);padding-bottom:9px;width:567px}
.main-head .bar{width:10px;height:31px;background:var(--orange)}
.main-head h3{font-family:"PT Sans Narrow",sans-serif;font-weight:400;font-size:23px;line-height:1;color:var(--red-title)}
.main-head p{font-family:"PT Sans Narrow",sans-serif;font-size:12px;color:var(--gray-sub);margin-top:1px}
.thumb{width:167px;height:97px;border-right:10px solid #eef6dc}
.green-title{font-family:"Arimo",sans-serif;font-weight:700;font-size:15px;color:var(--green-dark)}
.bullets{font-size:11.5px;line-height:23px;color:var(--link)}
.bullets li{list-style:none;display:flex;gap:14px}
.bullets li span{color:#555}
.promo{left:347px;top:995px;width:569px;height:124px;background:linear-gradient(90deg,#e9a23a 0,#8bb83a 38%,#6aa321 60%,#4f8f17 100%)}
.promo-photo{position:absolute;left:0;top:0;width:245px;height:124px;background:linear-gradient(90deg,#e9a23a,rgba(139,184,58,0))}
.promo h4{position:absolute;right:30px;top:18px;font-family:"Arimo",sans-serif;font-weight:700;font-style:italic;font-size:34px;letter-spacing:-1.5px;color:var(--white)}
.promo p{position:absolute;right:32px;top:56px;font-family:"PT Sans Narrow",sans-serif;font-weight:700;font-size:15px;color:#eaf3c8}
.promo .btn{position:absolute;right:30px;top:78px;width:120px;height:28px;border-radius:14px;background:linear-gradient(#fff,#e2e2e2);font-family:"PT Sans Narrow",sans-serif;font-weight:700;font-size:15px;color:#555;display:flex;align-items:center;justify-content:center;gap:6px}
.footer{left:63px;top:1125px;width:853px;height:75px;background:var(--footer);text-align:center;padding-top:27px;font-size:12px;color:var(--footer-text)}
</style>
</head>
<body>
<div class="sheet"></div>

<nav class="abs nav">
  <a>HOME PAGE</a><span class="sep"></span><a>ABOUT US</a><span class="sep"></span><a>OUR PRODUCTS</a><span class="sep"></span><a>SERVICES &amp; SUPPORT</a><span class="sep"></span><a>CASE STUDIES</a><span class="sep"></span><a>CONTACT</a>
</nav>

<div class="abs brand"><span class="mark"></span>Brivora</div>
<div class="abs follow">FOLLOW US ON:
  <span class="sq" style="background:#ef8a2a"></span>
  <span class="sq" style="background:#3b5d9a"></span>
  <span class="sq" style="background:#4cb3e3"></span>
</div>

<div class="abs tiles">
  <div class="tile"><h2>Cloud Software</h2><p>TOOLS FOR SPECIALTY BOARDS</p>
    <svg width="14" height="14" viewBox="0 0 14 14"><path d="M2 2 L11 11 M11 4 V11 H4" stroke="#fff" stroke-width="2.5" fill="none"/></svg></div>
  <div class="tile"><h2>Case Studies</h2><p>RESULTS FROM OUR CLIENTS</p>
    <svg width="14" height="14" viewBox="0 0 14 14"><path d="M2 2 L11 11 M11 4 V11 H4" stroke="#fff" stroke-width="2.5" fill="none"/></svg></div>
  <div class="tile"><h2>Client Stories</h2><p>KNOWLEDGE INTO IMPROVEMENT</p>
    <svg width="14" height="14" viewBox="0 0 14 14"><path d="M2 2 L11 11 M11 4 V11 H4" stroke="#fff" stroke-width="2.5" fill="none"/></svg></div>
</div>

<div class="abs hero">
  <div class="hero-photo" role="img" aria-label="Hero photograph for the Brivora home page"></div>
  <div class="badge"><div class="s1">Start</div><div class="s2">your free trial</div><div class="s3">Today!</div></div>
</div>

<div class="abs" style="left:78px;top:549px">
  <div class="sec-head">NEW ARTICLE</div>
  <div class="sec-sub">LOREM IPSUM DOLOR SIT AMET,</div>
</div>
<div class="abs item-title" style="left:80px;top:609px">
  <svg width="16" height="18" viewBox="0 0 16 18"><rect x="3" y="1" width="11" height="14" fill="#fff" stroke="#8a8a8a"/><rect x="1" y="3" width="11" height="14" fill="#f4f4f4" stroke="#8a8a8a"/><path d="M3 7h7M3 10h7M3 13h5" stroke="#9a9a9a"/></svg>
  Data into knowledge</div>
<div class="abs body" style="left:78px;top:631px;width:240px">
  <u>Morbi volutpat leo in ligula. Integer vel</u><br>bibendum sagittis. Fusce urna dui,<br>sollicitudin ac, pulvinar quis, tincidunt et
</div>
<div class="abs more" style="left:244px;top:713px"><i></i>read more</div>

<div class="abs" style="left:78px;top:758px">
  <div class="sec-head">OUR PRODUCTS</div>
  <div class="sec-sub">LOREM IPSUM DOLOR SIT AMET,</div>
</div>

<div class="abs item-title" style="left:79px;top:818px">
  <svg width="18" height="14" viewBox="0 0 18 14"><rect x=".5" y=".5" width="17" height="13" fill="#fbe9c8" stroke="#b08a5a"/><rect x=".5" y=".5" width="17" height="3" fill="#d08a3a"/><path d="M3 7h12M3 10h12" stroke="#c0a070"/></svg>
  Board certification suite</div>
<div class="abs body lnk" style="left:78px;top:841px;width:250px">Lorem ipsum dolor sit amet, consectetuer<br>adipiscing elit. Nam eu aLorem ipsum dolor</div>

<div class="abs item-title" style="left:79px;top:909px">
  <svg width="18" height="14" viewBox="0 0 18 14"><rect x=".5" y=".5" width="17" height="13" fill="#fbe9c8" stroke="#b08a5a"/><rect x=".5" y=".5" width="17" height="3" fill="#d08a3a"/><path d="M3 7h12M3 10h12" stroke="#c0a070"/></svg>
  Outcomes dashboard</div>
<div class="abs body lnk" style="left:78px;top:932px;width:250px">Lorem ipsum dolor sit amet, consectetuer<br>adipiscing elit. Nam eu aLorem ipsum dolor</div>

<div class="abs item-title" style="left:79px;top:999px">
  <svg width="18" height="14" viewBox="0 0 18 14"><rect x=".5" y=".5" width="17" height="13" fill="#fbe9c8" stroke="#b08a5a"/><rect x=".5" y=".5" width="17" height="3" fill="#d08a3a"/><path d="M3 7h12M3 10h12" stroke="#c0a070"/></svg>
  Learning portal</div>
<div class="abs body lnk" style="left:78px;top:1022px;width:250px">Lorem ipsum dolor sit amet, consectetuer<br>adipiscing elit. Nam eu aLorem ipsum dolor</div>

<div class="abs more" style="left:244px;top:1084px"><i></i>read more</div>

<div class="abs main-head" style="left:349px;top:549px">
  <span class="bar"></span>
  <div><h3>TURN DATA INTO KNOWLEDGE</h3><p>LOREM IPSUM DOLOR SIT AMET, CONSECTETUER</p></div>
</div>
<div class="abs thumb" role="img" aria-label="Photo of a clinician reviewing data" style="left:350px;top:611px;background:linear-gradient(135deg,#e8e4dc,#c9b8a6)"></div>
<div class="abs" style="left:534px;top:610px;width:370px">
  <div class="green-title">Reporting made simple for boards</div>
  <div class="body"><u>Morbi volutpat leo in ligula. Integer vel magna. Quisque ut</u><br>magna et nisi bibendum sagittis. Fusce urna dui, sollicitudin<br>ac, pulvinar quis, tincidunt et, risus. Quisque a nunc eget<br>ante in ipsum auctor viverra. Donec sapien.</div>
</div>

<div class="abs main-head" style="left:349px;top:759px">
  <span class="bar"></span>
  <div><h3>KNOWLEDGE INTO IMPROVEMENT</h3><p>LOREM IPSUM DOLOR SIT AMET, CONSECTETUER</p></div>
</div>
<div class="abs thumb" role="img" aria-label="Photo of a care team meeting" style="left:350px;top:821px;background:linear-gradient(135deg,#ece6dc,#dcb48a)"></div>
<div class="abs" style="left:534px;top:820px;width:370px">
  <div class="green-title">Custom tools for specialty groups</div>
  <div class="body"><u>Morbi volutpat leo in ligula. Integer vel magna. Quisque ut</u><br>magna et nisi bibendum sagittis. Fusce urna dui, sollicitudin<br>ac, pulvinar quis, tincidunt et, risus. Quisque a nunc eget<br>ante in ipsum auctor viverra. Donec sapien.</div>
</div>
<ul class="abs bullets" style="left:361px;top:930px;width:550px">
  <li><span>+</span><u>Lorem ipsum dolor sit amet, consectetuer adipiscing elit. Nam eu aLorem ipsum dolor sit</u></li>
  <li><span>+</span><u>amet, consectetuer adipiscing elit. Nam eu nulla. Donec lobortis purus vel urna. Nunc</u></li>
</ul>

<div class="abs promo">
  <div class="promo-photo" role="img" aria-label="Promotional photo for the newsletter"></div>
  <h4>The power of insight</h4>
  <p>JOIN OUR MONTHLY NEWSLETTER</p>
  <div class="btn">READ MORE
    <svg width="12" height="8" viewBox="0 0 12 8"><path d="M0 4h9M6 1l3 3-3 3" stroke="#777" stroke-width="1.5" fill="none"/></svg></div>
</div>

<footer class="abs footer">HOME | ABOUT US | OUR PRODUCTS | SERVICES &amp; SUPPORT | CASE STUDIES | CONTACTS</footer>
</body>
</html>
```